Industrial & commercial facility maintenance flyer

Design a 2 sided flyer that outlines our core business unit services. One side shall be for our industrial maintenance division while the other will be focused on our commercial maintenance division.

Media from website here: https://files.vornelbox.net/share/7Kq29XzPw4RtLmYc8NdHe5JbVa

Target Market(s)

Industrial and commercial facility maintenance companies and professionals

Industry/Entity Type

Maintenance

Font styles to use
Serif

Colors
ffffff
2f73b4
0455a3
cfdfed

Requirements
Must have
• Several photos of each applicable service. Reference existing website (www.trelcorp.com). Use of the blue and grey scheme of our current logo.
Nice to have
• Our logo design across the top with our contact information on the bottom.

```html
<!DOCTYPE html>
<html lang="en">
<head>
<meta charset="utf-8">
<title>Trelford Maintenance Solutions – Retail &amp; Commercial Flyer</title>
<link rel="stylesheet" href="https://fonts.googleapis.com/css2?family=Bebas+Neue&family=Lato:ital,wght@0,300;0,400;0,700;1,300;1,900&family=Montserrat:wght@300;400;500&display=swap">
<style>
  :root{
    --white:#ffffff;
    --blue-mid:#2f73b4;
    --blue-deep:#0455a3;
    --blue-pale:#cfdfed;
    --blue-box1:#2a7cc6;
    --blue-box2:#0d5aac;
    --blue-box3:#0c4788;
    --ink:#1f1f1f;
    --grey-text:#555a60;
    --footer:#2e3136;
  }
  *{margin:0;padding:0;box-sizing:border-box}
  html,body{width:970px;height:1200px;overflow:hidden;background:var(--white)}
  .flyer{position:relative;width:970px;height:1200px;overflow:hidden;background:var(--white);font-family:'Lato',sans-serif}
  .hero-photo{position:absolute;left:0;top:0;width:970px;height:574px;
    background:linear-gradient(120deg,#1d2f7a 0%,#2c45a0 35%,#8a96a8 60%,#b9b2a4 80%,#6f5a4a 100%)}
  .hero-shapes{position:absolute;left:0;top:0}
  .logo{position:absolute;left:580px;top:58px;display:flex;align-items:center;gap:12px}
  .logo-mark{width:54px;height:54px;border-radius:50%;background:var(--blue-deep)}
  .logo-name{font-family:'Montserrat',sans-serif;font-weight:500;font-size:21px;color:var(--blue-deep);line-height:1.1}
  .logo-tagline{font-family:'Montserrat',sans-serif;font-weight:400;font-size:9px;letter-spacing:3px;color:var(--grey-text);margin-top:6px}
  .headline-band{position:absolute;left:0;top:309px;width:970px;height:161px}
  .headline{position:absolute;right:40px;top:322px;text-align:right;color:var(--white)}
  .headline-rule{width:400px;height:1px;background:var(--white);margin-left:auto;margin-bottom:14px}
  .headline-kicker{font-style:italic;font-weight:300;font-size:24px}
  .headline-main{font-style:italic;font-weight:900;font-size:35px;line-height:1.2;margin-top:4px}
  .service{position:absolute;left:479px;width:442px;padding:28px 22px 0 36px;color:var(--white)}
  .service h3{font-family:'Lato',sans-serif;font-weight:700;font-size:17px}
  .service .rule{width:56px;height:2px;background:var(--white);margin:12px 0 14px}
  .service p{font-size:11px;line-height:1.37;font-weight:400}
  .service-1{top:518px;height:199px;background:var(--blue-box1)}
  .service-2{top:717px;height:198px;background:var(--blue-box2);padding-top:46px}
  .service-3{top:915px;height:198px;background:var(--blue-box3);padding-top:30px}
  .intro{position:absolute;left:65px;top:612px;width:360px}
  .intro-kicker{font-family:'Montserrat',sans-serif;font-weight:300;font-size:24px;color:var(--blue-deep)}
  .intro-title{font-family:'Bebas Neue',sans-serif;font-size:36px;color:var(--ink);letter-spacing:1px;line-height:1.1}
  .intro-rule{width:86px;height:3px;background:var(--blue-deep);margin:8px 0 16px}
  .intro-lead{font-weight:400;font-size:17px;line-height:1.3;color:var(--blue-mid)}
  .intro-body{font-weight:400;font-size:12.5px;line-height:1.35;color:var(--grey-text);margin-top:18px}
  .photo-strip{position:absolute;left:0;top:0}
  .tile{position:absolute;top:895px;height:170px}
  .tile-1{left:114px;width:167px;background:linear-gradient(160deg,#e7e5df,#3f5aa8 55%,#2c2f3a)}
  .tile-2{left:292px;width:167px;background:linear-gradient(200deg,#c9c3b6,#f0f0ee 40%,#2b3b7c)}
  .footer{position:absolute;left:0;top:1080px;width:970px;height:120px;
    background:linear-gradient(180deg,#3a3d42,var(--footer));color:var(--white)}
  .contact{position:absolute;left:48px;top:44px;font-family:'Montserrat',sans-serif;font-size:13px}
  .contact-row{display:flex;align-items:center;gap:10px;height:26px}
  .contact-row svg{flex:none}
  .call{position:absolute;left:514px;top:52px;font-family:'Bebas Neue',sans-serif;font-size:40px;letter-spacing:2px}
</style>
</head>
<body>
<div class="flyer">
  <div class="hero-photo" role="img" aria-label="Photo of a maintenance worker in blue overalls and yellow gloves tightening a pipe valve with a wrench"></div>
  <svg class="hero-shapes" width="970" height="574" viewBox="0 0 970 574">
    <polygon points="0,0 229,0 788,192 720,200" fill="#1d56b0"/>
    <polygon points="229,0 970,0 970,120 788,192" fill="#ffffff"/>
    <polygon points="788,192 970,120 970,232" fill="#2a7cc6"/>
  </svg>
  <div class="logo">
    <div class="logo-mark"></div>
    <div>
      <div class="logo-name">Trelford Maintenance Solutions</div>
      <div class="logo-tagline">INDUSTRIAL · COMMERCIAL · RETAIL</div>
    </div>
  </div>
  <svg class="headline-band" width="970" height="161" viewBox="0 0 970 161">
    <polygon points="450,0 970,0 970,161 370,161" fill="#2f5fb4" fill-opacity="0.85"/>
  </svg>
  <div class="headline">
    <div class="headline-rule"></div>
    <div class="headline-kicker">OVER 40 YEARS OF EXPERIENCE IN</div>
    <div class="headline-main">FACILITY AND EQUIPMENT<br>MAINTENANCE</div>
  </div>

  <section class="intro">
    <div class="intro-kicker">Retail &amp; Commercial</div>
    <h2 class="intro-title">MAINTENANCE SOLUTIONS</h2>
    <div class="intro-rule"></div>
    <p class="intro-lead">Trelford Maintenance Solutions knows how important it is to convert window shoppers to paying customers and to move inventory off your shelves.</p>
    <p class="intro-body">We ensure that your business is always looking its best with our cost-effective maintenance programs and crews available 24/7 to take care of any equipment or facility malfunction as quickly as possible.</p>
  </section>

  <svg class="photo-strip" width="970" height="1200" viewBox="0 0 970 1200">
    <polygon points="28,1065 114,915 114,1065" fill="#1d56b0"/>
    <rect x="459" y="915" width="20" height="125" fill="#1d56b0"/>
  </svg>
  <div class="tile tile-1" role="img" aria-label="Photo of a technician carrying a toolbox beside a service van"></div>
  <div class="tile tile-2" role="img" aria-label="Photo of a technician taking notes while inspecting a washbasin"></div>

  <section class="service service-1">
    <h3>We service equipment as needed</h3>
    <div class="rule"></div>
    <p>Trelford Maintenance Solutions provides services to stand-alone stores and big box stores alike, malls, nightclubs, and more. We work to enhance your image by taking preventative measures, like inspecting equipment for signs of wear or failing components. We service equipment as needed, measuring either by usage or manufacturer recommendations. After maintenance and repairs, our technicians provide an indepth report on equipment conditions, analyze equipment failure, and discuss future prevention.</p>
  </section>
  <section class="service service-2">
    <h3>Vast range of services</h3>
    <div class="rule"></div>
    <p>Customers may not realize how much work and effort goes into maintaining a functional well-kept business, but Trelford Maintenance does. For your convenience, we offer a vast range of services to handle any issues that may occur or to help you expand your business, whether adding on to your existing location or moving to a new one.</p>
  </section>

  <footer class="footer">
    <div class="contact">
      <div class="contact-row">
        <svg width="11" height="14" viewBox="0 0 11 14"><path d="M5.5 0A5.5 5.5 0 0 0 0 5.5C0 9.5 5.5 14 5.5 14S11 9.5 11 5.5A5.5 5.5 0 0 0 5.5 0Zm0 7.6a2.1 2.1 0 1 1 0-4.2 2.1 2.1 0 0 1 0 4.2Z" fill="#fff"/></svg>
        <span>Trelford Maintenance Solutions, your city , Your Country</span>
      </div>
      <div class="contact-row">
        <svg width="13" height="9" viewBox="0 0 13 9"><rect x="0.5" y="0.5" width="12" height="8" fill="none" stroke="#fff"/><path d="M0.5 0.5 6.5 5 12.5 0.5" fill="none" stroke="#fff"/></svg>
        <span>info@trelcorp.com</span>
        <svg width="14" height="14" viewBox="0 0 14 14" style="margin-left:24px"><circle cx="7" cy="7" r="6.3" fill="none" stroke="#fff"/><ellipse cx="7" cy="7" rx="2.8" ry="6.3" fill="none" stroke="#fff"/><path d="M0.7 7h12.6" stroke="#fff"/></svg>
        <span>www.trelcorp.com</span>
      </div>
    </div>
    <div class="call">CALL US &nbsp;- &nbsp;1800-555-0199</div>
  </footer>

  <section class="service service-3">
    <h3>Install and Repair services</h3>
    <div class="rule"></div>
    <p>We install doors, restroom partitions, storefronts, flooring, and plumbing. Repairs include doors, storefronts, flooring, building exteriors, plumbing, appliances, fencing, and loading docks. We take care of landscaping, snow removal, irrigation systems, pest control, and other seasonal maintenance as need be when the weather changes.</p>
  </section>
</div>
</body>
</html>
```